Beautiful app design for Trellin Apps

Trellin Apps makes apps for small businesses, primarily restaurants. We need a beautiful new design to update our apps with. The app design should be flexible so that it can be used as a template for several different restaurants. Interchangeable background images, fonts, and themes would be nice so that these can be applied to different restaurant types.
Updates

Target Market(s)

The target market is restaurant owners who will use the app to promote their restaurants.

Industry/Entity Type

Restaurant

Requirements
Must have
• Screens: Splash, main menu, top food menu, inner food menu or section, food menu item detail, specials page, beer menu, inner beer menu or section, beer detail page, social media menu, and About Us section. Please see screenshot images from current app for examples.
Nice to have
• Interchangeable themes, colors, fonts, and background images if applicable.

```html
<!DOCTYPE html>
<html lang="en">
<head>
<meta charset="utf-8">
<title>Trellin Apps – Menu</title>
<link href="https://fonts.googleapis.com/css2?family=Nunito+Sans:wght@400;600;800;900&display=swap" rel="stylesheet">
<style>
  :root {
    --stage: #29252b;
    --screen-bg: #e9e6e5;
    --card: #f4f1f0;
    --card-edge: #d9d4d3;
    --red: #e0202f;
    --red-dark: #a8111e;
    --bar-top: #7a0f18;
    --ink: #1d2340;
    --muted: #5c5d66;
    --tab-bg: #1f1c21;
    --tab-ink: #e8e6ea;
    --btn-edge: #bdbdbd;
  }
  * { box-sizing: border-box; margin: 0; padding: 0; }
  html, body { width: 1200px; height: 900px; overflow: hidden; }
  body {
    background: var(--stage);
    font-family: "Nunito Sans", sans-serif;
    display: flex; align-items: center; justify-content: center;
  }
  .app-screen {
    width: 480px; height: 852px;
    background: var(--screen-bg);
    display: flex; flex-direction: column;
    overflow: hidden;
    box-shadow: 0 20px 50px rgba(0,0,0,.45);
  }
  .status-bar {
    flex: 0 0 30px; background: var(--bar-top); color: #fff;
    display: flex; align-items: center; justify-content: space-between;
    padding: 0 12px; font-size: 15px; font-weight: 600;
  }
  .status-left, .status-right { display: flex; align-items: center; gap: 6px; width: 120px; }
  .status-right { justify-content: flex-end; }
  .signal { display: flex; gap: 3px; }
  .signal i { width: 7px; height: 7px; border-radius: 50%; background: #fff; display: block; }
  .signal i.off { background: transparent; border: 1px solid #fff; }
  .nav-bar {
    flex: 0 0 66px; position: relative;
    background: linear-gradient(#e8283a, var(--red) 50%, #c81524);
    display: flex; align-items: center; justify-content: space-between;
    padding: 0 12px; border-bottom: 1px solid var(--red-dark);
  }
  .nav-title {
    position: absolute; left: 0; right: 0; text-align: center;
    color: #fff; font-size: 28px; font-weight: 900; pointer-events: none;
  }
  .nav-button {
    position: relative; z-index: 1;
    color: #fff; font-size: 19px; font-weight: 800;
    padding: 8px 20px; border-radius: 22px;
    background: linear-gradient(#e42a3b, #c3131f);
    border: 2px solid #f04d5a;
    box-shadow: inset 0 1px 0 rgba(255,255,255,.25), 0 1px 2px rgba(0,0,0,.3);
  }
  .menu-list {
    flex: 1 1 auto; min-height: 0; overflow: hidden;
    padding: 8px 10px 0; display: flex; flex-direction: column; gap: 8px;
  }
  .menu-item {
    flex: 0 0 136px; position: relative;
    background: var(--card); border: 1px solid var(--card-edge); border-radius: 6px;
    display: grid; grid-template-columns: 120px minmax(0, 1fr); gap: 0 16px;
    padding: 12px 18px 12px 12px;
  }
  .item-photo {
    width: 120px; height: 84px; border: 3px solid #fff; border-radius: 3px;
    box-shadow: 0 1px 3px rgba(0,0,0,.25);
  }
  .photo-prawn { background: linear-gradient(135deg, #c5a887, #6f8a4a 55%, #9b7b5a); }
  .photo-blt { background: linear-gradient(160deg, #b77a3e, #d8c77e 50%, #6aa04a); }
  .photo-cucumber { background: linear-gradient(135deg, #7a5c3d, #c89a5a 50%, #e8e0c8); }
  .photo-chicken { background: linear-gradient(160deg, #7fc1e0, #4e7a3a 45%, #9a6b45); }
  .item-info { min-width: 0; }
  .item-name { font-size: 21px; font-weight: 900; color: var(--ink); line-height: 1.15; white-space: nowrap; }
  .item-size { font-size: 15px; color: var(--muted); margin-top: 2px; }
  .stepper { display: flex; align-items: center; gap: 6px; margin-top: 6px; }
  .step-btn {
    width: 38px; height: 32px; border-radius: 4px;
    background: linear-gradient(#fff, #e4e4e4); border: 1px solid var(--btn-edge);
    font-size: 24px; font-weight: 900; color: #333; line-height: 28px; text-align: center;
  }
  .step-count {
    width: 46px; height: 32px; background: #d8d8d8; border: 1px solid #c4c4c4;
    font-size: 19px; font-weight: 800; color: #333; text-align: center; line-height: 30px;
  }
  .item-price {
    position: absolute; right: 18px; bottom: 12px;
    font-size: 26px; font-weight: 900; color: var(--ink); line-height: 1;
  }
  .tab-bar {
    flex: 0 0 74px; background: var(--tab-bg); position: relative; z-index: 2;
    display: grid; grid-template-columns: repeat(4, 1fr);
    border-top: 1px solid #000;
  }
  .tab {
    display: flex; flex-direction: column; align-items: center; justify-content: center; gap: 6px;
    color: var(--tab-ink); font-size: 11px; font-weight: 800; letter-spacing: .5px;
    border-right: 1px solid #2f2b31;
  }
  .tab svg { width: 28px; height: 28px; }
  .tab-active { color: var(--red); background: #17141a; border-bottom: 3px solid var(--red); }
</style>
</head>
<body>
<main class="app-screen">
  <div class="status-bar">
    <div class="status-left">
      <span class="signal"><i></i><i></i><i></i><i class="off"></i><i class="off"></i></span>
      <svg width="16" height="12" viewBox="0 0 16 12"><path d="M1 4a10 10 0 0 1 14 0M3.5 6.5a6.5 6.5 0 0 1 9 0M6 9a3 3 0 0 1 4 0" fill="none" stroke="#fff" stroke-width="1.6"/></svg>
    </div>
    <span class="status-time">4:21 PM</span>
    <div class="status-right">
      <svg width="9" height="14" viewBox="0 0 9 14"><path d="M1 4l7 6-3.5 3V1L8 4l-7 6" fill="none" stroke="#fff" stroke-width="1.3"/></svg>
      <span>22%</span>
      <svg width="26" height="12" viewBox="0 0 26 12"><rect x=".5" y=".5" width="22" height="11" rx="2" fill="none" stroke="#fff"/><rect x="2" y="2" width="5" height="8" fill="#fff"/><rect x="23" y="4" width="2" height="4" fill="#fff"/></svg>
    </div>
  </div>

  <header class="nav-bar">
    <span class="nav-button">Back</span>
    <h1 class="nav-title">Menu</h1>
    <span class="nav-button">Order</span>
  </header>

  <section class="menu-list">
    <article class="menu-item">
      <div class="item-photo photo-prawn" role="img" aria-label="Photo of a tartare prawn sandwich"></div>
      <div class="item-info">
        <h2 class="item-name">Tartare Prawn Sandwich</h2>
        <p class="item-size">Size: Large</p>
        <div class="stepper"><span class="step-btn">−</span><span class="step-count">3</span><span class="step-btn">+</span></div>
      </div>
      <p class="item-price">$8.99</p>
    </article>
    <article class="menu-item">
      <div class="item-photo photo-blt" role="img" aria-label="Photo of a classic BLT sandwich"></div>
      <div class="item-info">
        <h2 class="item-name">Classic BLT</h2>
        <p class="item-size">Size: Large</p>
        <div class="stepper"><span class="step-btn">−</span><span class="step-count">1</span><span class="step-btn">+</span></div>
      </div>
      <p class="item-price">$6.95</p>
    </article>
    <article class="menu-item">
      <div class="item-photo photo-cucumber" role="img" aria-label="Photo of a cheesy cucumber toasted sandwich"></div>
      <div class="item-info">
        <h2 class="item-name">Cheesy Cucumber Special</h2>
        <p class="item-size">Size: Large</p>
        <div class="stepper"><span class="step-btn">−</span><span class="step-count">2</span><span class="step-btn">+</span></div>
      </div>
      <p class="item-price">$6.95</p>
    </article>
    <article class="menu-item">
      <div class="item-photo photo-chicken" role="img" aria-label="Photo of a grilled chicken sandwich"></div>
      <div class="item-info">
        <h2 class="item-name">Grilled Chicken Sandwich</h2>
        <p class="item-size">Size: Large</p>
        <div class="stepper"><span class="step-btn">−</span><span class="step-count">3</span><span class="step-btn">+</span></div>
      </div>
      <p class="item-price">$5.00</p>
    </article>
    <article class="menu-item">
      <div class="item-photo photo-blt" role="img" aria-label="Photo of a classic BLT sandwich"></div>
      <div class="item-info">
        <h2 class="item-name">Classic BLT</h2>
        <p class="item-size">Size: Large</p>
      </div>
    </article>
  </section>

  <nav class="tab-bar">
    <div class="tab">
      <svg viewBox="0 0 28 28"><path d="M4 14L14 5l10 9M7 12v11h14V12M12 23v-6h4v6" fill="none" stroke="currentColor" stroke-width="1.8"/></svg>
      HOME
    </div>
    <div class="tab">
      <svg viewBox="0 0 28 28"><path d="M6 9a4 4 0 0 1 5-4 5 5 0 0 1 8 1 3.5 3.5 0 0 1 2 6v12H8V12a3 3 0 0 1-2-3z" fill="currentColor"/><path d="M21 14h2a2 2 0 0 1 2 2v3a2 2 0 0 1-2 2h-2" fill="none" stroke="currentColor" stroke-width="2"/></svg>
      BEERS
    </div>
    <div class="tab tab-active">
      <svg viewBox="0 0 28 28"><path d="M3 6l11 3 11-3v16l-11 3-11-3zM14 9v16" fill="none" stroke="currentColor" stroke-width="1.8"/></svg>
      MENU
    </div>
    <div class="tab">
      <svg viewBox="0 0 28 28"><circle cx="11" cy="9" r="4" fill="none" stroke="currentColor" stroke-width="1.8"/><path d="M4 23a7 7 0 0 1 14 0z" fill="none" stroke="currentColor" stroke-width="1.8"/><circle cx="18" cy="10" r="3.5" fill="none" stroke="currentColor" stroke-width="1.6"/><path d="M19 16a6 6 0 0 1 6 7h-5" fill="none" stroke="currentColor" stroke-width="1.6"/></svg>
      SOCIAL
    </div>
  </nav>
</main>
</body>
</html>
```